Seafarer Moon Brook Spring, Water Bottle Label Design

We require a logo and label design for water bottling business called "Seafarer Moon Brook Spring"
the logo should be a simple 2 tone, pirates skull & cross bones style, so it can be embossed on the glass bottle.

For the bottle label we would like to see a narrow front label in parchment style scroll, burnt edges, treasure map feel. - see attached file.
For the back side label we would something a little larger of the same style label but double sided with the map of Tasmania on the inside, so it can be seen through the bottle. - see attached image.
on the outside of the back label we will have the relevant information about our business, webpage and social media links.
a successful applicant may have the opportunity to create our webpage also.

Pirate Themed, Ye olde Style Parchment, simple colours, faded looking old vintage.

Target Market(s)

Children, Chinese, Tourist

Industry/Entity Type

Water Company

Contact Information for Business Card

Rosalind Whitcombe
Webpage, Social Media. Address

Logo Text

Seafarer Moon Brook Spring

Font styles to use
Script

Colors

Designer to choose colors to be used in the design.

Requirements
Must have
• Pirate Themed, Ye olde Style Parchment, simple colours, faded looking old vintage.
Nice to have
• simple but elegant

```html
<!DOCTYPE html>
<html lang="en">
<head>
<meta charset="utf-8">
<title>Seafarer Moon Brook Spring – Bottle Labels</title>
<link rel="stylesheet" href="https://fonts.googleapis.com/css2?family=Pirata+One&display=swap">
<style>
  :root {
    --page: #ffffff;
    --parchment-light: #f7e6b0;
    --parchment-mid: #ecc97a;
    --parchment-dark: #d49a3e;
    --parchment-stain: #c8893a;
    --burnt-edge: #8a5218;
    --burnt-deep: #5e3510;
    --back-paper: #f8f5ee;
    --back-paper-shade: #ebe5d6;
    --gold-rim: #dba640;
    --gold-bright: #f2c84e;
    --gold-deep: #9c6a1a;
    --emblem-dark: #2f3235;
    --emblem-mid: #5b5f63;
    --ink: #3b3d40;
    --ink-soft: #2a2a2a;
    --map-tint: #e6dcc6;
  }
  html, body {
    margin: 0;
    padding: 0;
    width: 1200px;
    height: 539px;
    overflow: hidden;
    background: var(--page);
  }
  .label-sheet {
    display: block;
    width: 1200px;
    height: 539px;
  }
  .brand-name {
    font-family: "Pirata One", serif;
    fill: var(--ink);
    font-weight: 400;
    text-anchor: middle;
  }
  .front-label__name { font-size: 50px; }
  .front-label__name-foot { font-size: 62px; }
  .back-label__title { font-size: 32px; }
  .info-line {
    stroke: var(--ink-soft);
    stroke-width: 2;
    stroke-dasharray: 2 2;
  }
</style>
</head>
<body>
<svg class="label-sheet" viewBox="0 0 1300 584" xmlns="http://www.w3.org/2000/svg" role="img" aria-label="Seafarer Moon Brook Spring front and back bottle labels">
  <defs>
    <radialGradient id="parchment-fill" cx="50%" cy="45%" r="68%">
      <stop offset="0%" stop-color="var(--parchment-light)"/>
      <stop offset="60%" stop-color="var(--parchment-mid)"/>
      <stop offset="100%" stop-color="var(--parchment-dark)"/>
    </radialGradient>
    <radialGradient id="stain-fill" cx="50%" cy="50%" r="50%">
      <stop offset="0%" stop-color="var(--parchment-stain)" stop-opacity="0.45"/>
      <stop offset="100%" stop-color="var(--parchment-stain)" stop-opacity="0"/>
    </radialGradient>
    <linearGradient id="emblem-band" x1="0" y1="0" x2="1" y2="0">
      <stop offset="0%" stop-color="var(--gold-deep)"/>
      <stop offset="45%" stop-color="var(--gold-bright)"/>
      <stop offset="100%" stop-color="var(--gold-deep)"/>
    </linearGradient>
    <linearGradient id="emblem-core" x1="0" y1="0" x2="1" y2="1">
      <stop offset="0%" stop-color="var(--emblem-mid)"/>
      <stop offset="100%" stop-color="var(--emblem-dark)"/>
    </linearGradient>
    <linearGradient id="back-paper-fill" x1="0" y1="0" x2="0" y2="1">
      <stop offset="0%" stop-color="var(--back-paper-shade)"/>
      <stop offset="40%" stop-color="var(--back-paper)"/>
      <stop offset="100%" stop-color="var(--back-paper)"/>
    </linearGradient>
    <linearGradient id="back-rim" x1="0" y1="0" x2="1" y2="1">
      <stop offset="0%" stop-color="var(--parchment-dark)"/>
      <stop offset="50%" stop-color="var(--gold-bright)"/>
      <stop offset="100%" stop-color="var(--gold-rim)"/>
    </linearGradient>
    <path id="front-title-arc" d="M55 175 Q300 45 548 175"/>
    <path id="back-title-arc" d="M790 132 Q975 40 1165 120"/>
  </defs>

  <!-- Front label -->
  <g class="front-label">
    <path class="front-label__shape" role="img" aria-label="Aged parchment treasure map background with burnt edges"
          d="M96 22 L140 16 L190 24 L250 14 L310 22 L370 15 L430 23 L470 17 L505 24
             L528 52 L552 82 L548 140 L556 210 L549 280 L555 345 L550 398
             L470 452 L400 500 L340 540 L300 562 L255 538 L190 498 L120 452 L48 400
             L44 330 L50 260 L43 190 L49 120 L46 82 L70 52 Z"
          fill="url(#parchment-fill)" stroke="var(--burnt-edge)" stroke-width="6" stroke-linejoin="round"/>
    <g class="front-label__stains" aria-hidden="true">
      <ellipse cx="110" cy="240" rx="60" ry="80" fill="url(#stain-fill)"/>
      <ellipse cx="500" cy="300" rx="55" ry="90" fill="url(#stain-fill)"/>
      <ellipse cx="280" cy="60" rx="120" ry="35" fill="url(#stain-fill)"/>
      <ellipse cx="160" cy="440" rx="70" ry="40" fill="url(#stain-fill)"/>
      <ellipse cx="450" cy="430" rx="60" ry="35" fill="url(#stain-fill)"/>
    </g>
    <path class="front-label__burn" aria-hidden="true"
          d="M96 22 L140 16 L190 24 L250 14 L310 22 L370 15 L430 23 L470 17 L505 24"
          fill="none" stroke="var(--burnt-deep)" stroke-width="4" opacity="0.6"/>
    <g class="front-label__emblem" role="img" aria-label="Pirate skull and crossbones emblem artwork">
      <rect x="100" y="150" width="400" height="300" rx="30" fill="url(#emblem-band)" opacity="0.9"/>
      <rect x="155" y="165" width="290" height="260" rx="26" fill="url(#emblem-core)"/>
    </g>
    <text class="brand-name front-label__name"><textPath href="#front-title-arc" startOffset="50%">Seafarer Moon Brook</textPath></text>
    <text class="brand-name front-label__name-foot" x="300" y="505">Spring</text>
  </g>

  <!-- Back label -->
  <g class="back-label">
    <path class="back-label__shape"
          d="M775 20 L1180 20 L1225 80 L1225 400 L975 565 L728 400 L728 80 Z"
          fill="url(#back-paper-fill)" stroke="url(#back-rim)" stroke-width="8" stroke-linejoin="round"/>
    <circle class="back-label__compass" role="img" aria-label="Faded compass rose"
            cx="805" cy="140" r="50" fill="var(--map-tint)" opacity="0.6"/>
    <path class="back-label__map" role="img" aria-label="Faded map of Tasmania with a dotted voyage route"
          d="M770 220 Q980 200 1200 230 L1200 390 L975 520 L770 390 Z"
          fill="var(--map-tint)" opacity="0.3"/>
    <text class="brand-name back-label__title"><textPath href="#back-title-arc" startOffset="50%">Seafarer Moon Brook Spring</textPath></text>
    <g class="back-label__info-lines">
      <line class="info-line" x1="820" y1="217" x2="1128" y2="217"/>
      <line class="info-line" x1="820" y1="246" x2="1128" y2="246"/>
      <line class="info-line" x1="820" y1="276" x2="1128" y2="276"/>
      <line class="info-line" x1="820" y1="305" x2="1128" y2="305"/>
      <line class="info-line" x1="820" y1="334" x2="1128" y2="334"/>
      <line class="info-line" x1="820" y1="364" x2="1128" y2="364"/>
      <line class="info-line" x1="820" y1="393" x2="1128" y2="393"/>
      <line class="info-line" x1="900" y1="423" x2="1048" y2="423"/>
    </g>
  </g>
</svg>
</body>
</html>
```